Mix Comet business cards + chance to win packaging and other design projects

including logo already designed.

******** I need 2 business cards:
1. that is general for the company
2. that is specific for me

*********On the reverse side of the business card I want it to be divided into 4 boxes and each box to describe a stage in how to use the product. I need the boxes to be numbered and the contents to be easy to absorb and include graphics showing the actions also.
Turning then photo's into simplified, cool illustrations** would be really cool. This would allow changes, like writing "water" on the bottle etc etc. Maybe have a fftness lady drinking at the end? Imagination over to you.
The photo's are of the prototype so the illustrations can replace the grey caps with bright orange etc etc

CAPTIONS FOR ILLUSTRATIONS
1. Charge the Mix Comet
2.The Mix Comet is now ready for making a shake anywhere, anytime !
3. Choose any bottled water or beverage, release shot cap and Jet powder in.
4. Shake bottle, enjoy!
Updates

Can you illustrate?
I just changed the photos and captions to simplify.
Please re read the brief, thanks

Target Market(s)

Fitness, weight loss, health
male and female
any potential powdered drink user.

quince, skyroam design style ? Clean, simple, bold, clever, cool

Industry/Entity Type

Business

Requirements
Must have
• Must have logo and mixcomet.com

Card 1: email: info@mixcomet.com

Card 2: Rafe Dunmore LL.b. /President/ email:rafe@mixcomet.com/ office: 415 382 6619/ direct: 628 741 3085

I want the card to have a white background, not color blocked in.

I have included photos of the type of illustrations needed in each box.
In the illustrations pls make the mix comet army green and the caps bright orange.
Get the point across as simply as you can. Make it cool pls :)

```html
<!DOCTYPE html>
<html lang="en">
<head>
<meta charset="utf-8">
<title>Mix Comet business cards</title>
<link rel="stylesheet" href="https://fonts.googleapis.com/css2?family=Open+Sans:wght@400;600;800&display=swap">
<style>
  :root {
    --page: #d6d6d4;
    --card: #ffffff;
    --panel: #e6e6e6;
    --orange: #ee5a1c;
    --navy: #283a6b;
    --text-grey: #6e6e6e;
    --text-dark: #555555;
    --bubble: #c9c9c9;
    --icon-tone: #c7cad6;
  }
  * { box-sizing: border-box; margin: 0; padding: 0; }
  html, body {
    width: 1200px; height: 728px; overflow: hidden;
    background: var(--page);
    font-family: "Open Sans", Arial, sans-serif;
  }
  .canvas { position: relative; width: 1200px; height: 728px; }

  .card {
    position: absolute;
    background: var(--card);
    overflow: hidden;
  }
  .card--front { left: 102px; top: 151px; width: 463px; height: 283px; }
  .card--back  { left: 657px; top: 282px; width: 465px; height: 284px; }

  .bubble-field {
    position: absolute;
    background: radial-gradient(ellipse at 60% 50%, rgba(201,201,201,0.55) 0%, rgba(201,201,201,0.25) 50%, rgba(201,201,201,0) 75%);
  }
  .card--front .bubble-field { left: 150px; top: 30px; width: 313px; height: 245px; }
  .card--back .bubble-field { left: 170px; top: 60px; width: 295px; height: 224px; }

  .wordmark {
    position: absolute;
    color: var(--orange);
    font-weight: 800;
    text-transform: uppercase;
    letter-spacing: 0.02em;
    white-space: nowrap;
    display: flex; align-items: center;
  }
  .wordmark__dot {
    display: inline-block;
    border-radius: 50%;
    background: var(--orange);
  }
  .card--front .wordmark { left: 84px; top: 98px; font-size: 40px; gap: 12px; }
  .card--front .wordmark__dot { width: 14px; height: 14px; }
  .card--back .wordmark { left: 24px; top: 22px; font-size: 23px; gap: 7px; }
  .card--back .wordmark__dot { width: 8px; height: 8px; }

  .website {
    position: absolute;
    left: 0; right: 0; top: 242px;
    text-align: center;
    font-size: 16px;
    color: var(--text-grey);
    letter-spacing: 0.02em;
  }

  .contact-email {
    position: absolute;
    right: 26px; top: 30px;
    font-size: 15px;
    color: #9a9a9a;
  }
  .contact-email span { color: var(--text-dark); }

  .steps-panel {
    position: absolute;
    left: 0; top: 86px; width: 465px; height: 198px;
    background: var(--panel);
  }
  .step {
    position: absolute;
    top: 0; width: 140px;
    margin-left: -70px;
    text-align: center;
  }
  .step:nth-child(2) { left: 61px; }
  .step:nth-child(3) { left: 152px; }
  .step:nth-child(4) { left: 276px; }
  .step:nth-child(5) { left: 399px; }
  .step__art {
    display: block;
    width: 62px; height: 78px;
    margin: 8px auto 0;
    border-radius: 8px;
    background: linear-gradient(160deg, var(--icon-tone), #dcdde4);
  }
  .step__caption {
    position: absolute;
    left: 0; right: 0; top: 96px;
    font-size: 13px;
    line-height: 22px;
    color: var(--text-grey);
    white-space: nowrap;
  }
  .step__number {
    position: absolute;
    left: 50%; top: 171px;
    margin-left: -7px;
    width: 14px; height: 14px;
    border-radius: 50%;
    background: var(--orange);
    color: #fff;
    font-size: 9px; font-weight: 600;
    line-height: 14px;
  }
</style>
</head>
<body>
<main class="canvas">

  <section class="card card--front" aria-label="Company card, front">
    <div class="bubble-field" role="img" aria-label="Scattered soft grey bubbles"></div>
    <div class="wordmark"><span class="wordmark__dot"></span>Mix Comet</div>
    <p class="website">www. mixcomet.com</p>
  </section>

  <section class="card card--back" aria-label="Company card, how to use">
    <div class="wordmark"><span class="wordmark__dot"></span>Mix Comet</div>
    <p class="contact-email">email: <span>info@mixcomet.com</span></p>

    <div class="steps-panel">
      <div class="bubble-field" role="img" aria-label="Scattered soft grey bubbles"></div>
      <div class="step">
        <span class="step__art" role="img" aria-label="Line illustration: scoop pouring powder into the dispenser"></span>
        <p class="step__caption">Charge the<br>Mix Comet</p>
        <span class="step__number">1</span>
      </div>
      <div class="step">
        <span class="step__art" role="img" aria-label="Line illustration: hand holding the charged dispenser"></span>
        <p class="step__caption">Making a shake<br>anywhere,<br>anytime !</p>
        <span class="step__number">2</span>
      </div>
      <div class="step">
        <span class="step__art" role="img" aria-label="Line illustration: dispenser releasing powder into a water bottle"></span>
        <p class="step__caption">Choose any bottled<br>water, release shot<br>cap and Jet powder in</p>
        <span class="step__number">3</span>
      </div>
      <div class="step">
        <span class="step__art" role="img" aria-label="Line illustration: drinking from the shaken bottle"></span>
        <p class="step__caption">Shake bottle,<br>enjoy!</p>
        <span class="step__number">4</span>
      </div>
    </div>
  </section>

</main>
</body>
</html>
```